Northfield Energy Product Distribution Brochure

We are looking to have our current brochure for our customers completely redesigned...the idea is to present the relevant information in an attractive way . Our website is northfieldenergy-example.com where you can find more information about us. We have included a file with a rough idea of the page order and what each should include but feel free to adapt based on design. The example provided is only for context and doesnt have to be maintained. We will be using the brochure both digitally and in print form. As long as it reads easily and is eye catching, the design can be horizontal or vertical.Final deliverable should be indesign file.

"Our Brands" page: should be limited to one page (space being enough) where it has the header for each one (for example diesel generators) space for one or two lines of text and then the corresponding logos for each of the five categories
Updates

For those asking: the "our brands" page should be a single page layout where there is a header with the corresponding section and space for maybe one line of text followed by the two logos for that category. Each of the product pages should be similar in fashion to the one in the document attached: a photo of the product with some white space and space for the text to be included. We will be posting additional examples today

Target Market(s)

We want to present it to customers both digitally and in print so they can see our products

Industry/Entity Type

Power Generation

Font styles to use
Serif

Requirements
Must have
• Eye catching and able to present the information in a presentable fashion. Rest is up to you.
Nice to have
• Should incorporate the colors of our logo but can also add other depending on design

```html
<!DOCTYPE html>
<html lang="en">
<head>
<meta charset="utf-8">
<title>Northfield Energy – Distributor Program Guide</title>
<link rel="stylesheet" href="https://fonts.googleapis.com/css2?family=Merriweather:wght@300;400;700;900&display=swap">
<style>
:root{
  --bg:#5f5f5f;
  --paper:#ffffff;
  --paper-grey:#e6e6e8;
  --ink:#1e1e1e;
  --ink-soft:#3a3a3a;
  --dark:#2b2b2d;
  --yellow:#f7b918;
  --yellow-deep:#f29a0c;
  --orange:#e8730c;
}
*{box-sizing:border-box;margin:0;padding:0}
html,body{width:1200px;height:1200px;overflow:hidden;background:var(--bg);font-family:"Merriweather",Georgia,serif;color:var(--ink)}
.spread{position:absolute;left:334px;width:560px;height:362px;display:flex;box-shadow:0 6px 10px rgba(0,0,0,.35)}
.spread--1{top:21px}.spread--2{top:416px}.spread--3{top:808px}
.page{position:relative;width:280px;height:362px;overflow:hidden}
.page--left{background:linear-gradient(90deg,#eeeeef 0%,#e9e9eb 80%,#cfcfd2 100%)}
.page--right{background:linear-gradient(90deg,#c9c9cc 0%,#eeeeef 18%,#eeeeef 100%)}
.page__header{position:absolute;top:0;left:0;right:0;height:27px;background:var(--paper)}
.page__num{position:absolute;top:10px;font-size:6.5px;font-weight:700}
.page--left .page__num{left:26px}
.page__running{position:absolute;top:11px;left:96px;font-size:4.6px;font-weight:700}
.page__running span{font-weight:400}
.page__footer{position:absolute;bottom:0;left:0;right:0;height:24px;background:var(--paper)}
.page--right .page__footer .page__running{top:10px;left:95px}
.page--right .page__footer .page__num{right:26px;top:9px}
.brandmark{position:absolute;display:flex;align-items:center;gap:2px;font-size:3.6px;font-weight:700;color:var(--yellow-deep)}
.brandmark i{width:5px;height:5px;background:var(--dark);display:block}
.deco{position:absolute;inset:0;pointer-events:none}
.title{position:absolute;top:45px;left:0;right:0;text-align:center;font-size:16px;font-weight:300;color:var(--ink-soft)}
.title b{font-weight:700;color:var(--ink)}
.photo{position:absolute;border-radius:3px}
.brandbox{position:absolute;left:203px;top:100px;width:57px;height:40px;background:#fff;border:1.3px solid var(--dark);border-radius:5px;display:flex;flex-direction:column;justify-content:center;align-items:center;gap:3px;font-weight:900;font-size:4.4px;text-align:center;line-height:1.1}
.brandbox .r{color:#d3261e}.brandbox .k{color:var(--ink)}.brandbox .g{color:#8a8a8a}
.features{position:absolute;left:33px;top:206px;width:190px;font-size:3.4px;line-height:1.45;color:var(--ink)}
.page--right .features{left:32px}
.features h4{font-size:4.2px;font-weight:900}
.features ul{padding-left:5px}
.photo-city{position:absolute;inset:0;background:linear-gradient(180deg,#8fa0b8 0%,#6c7fa0 25%,#c48b6a 45%,#3a3a48 60%,#15151d 100%)}
.tag{position:absolute;height:7px;background:var(--dark);color:var(--yellow);font-size:4.4px;font-weight:700;display:flex;align-items:center;justify-content:center}
.cols{position:absolute;top:93px;left:26px;right:22px;display:flex;gap:12px;font-size:3.2px;line-height:1.35}
.cols ul{flex:1;padding-left:5px}
.cols li{margin-bottom:4px}
.location{position:absolute;top:208px;left:26px;width:112px;font-size:3.1px;line-height:1.4}
.location p{margin-bottom:4px}
.contact{position:absolute;top:210px;left:151px;width:120px;font-size:4.1px;font-weight:700;line-height:1.35}
.contact .row{display:flex;align-items:flex-start;gap:5px;margin-bottom:7px}
.contact svg{flex:none;width:6px;height:6px}
.divider{position:absolute;left:145px;top:200px;width:.6px;height:90px;background:#999}
</style>
</head>
<body>

<!-- Spread 1: pages 8–9 -->
<section class="spread spread--1">
  <article class="page page--left">
    <header class="page__header"><span class="page__num">8</span><span class="page__running">DISTRIBUTOR <span>PROGRAM GUIDE</span></span></header>
    <svg class="deco" viewBox="0 0 280 362">
      <rect x="0" y="27" width="280" height="2" fill="#f7b918"/><rect x="0" y="29" width="280" height="7" fill="#2b2b2d"/>
      <circle cx="140" cy="150" r="62" fill="#f7b918"/>
      <path d="M140 88 H233 V100" fill="none" stroke="#f7b918" stroke-width="1.3"/>
      <rect x="266" y="140" width="3" height="180" fill="#f7b918"/><rect x="272" y="160" width="1.5" height="160" fill="#e8730c"/>
      <rect x="0" y="318" width="280" height="3" fill="#f7b918"/><rect x="0" y="321" width="280" height="6" fill="#2b2b2d"/>
    </svg>
    <h2 class="title">AC <b>Alternators</b></h2>
    <div class="photo" role="img" aria-label="Photo of a black industrial AC alternator" style="left:38px;top:92px;width:150px;height:98px;background:linear-gradient(135deg,#555 0%,#1d1d1f 60%,#0e0e10 100%)"></div>
    <div class="brandbox"><span><span class="r">MERIDIAN</span> | <span class="r">KESTREL</span></span><span class="k">LAURENT<br>MOTEURS</span></div>
    <div class="features"><h4>FEATURES:</h4><ul>
      <li>Class H insulation throughout.</li><li>Standard 12-wire reconnectable winding, 2/3 pitch.</li><li>Voltage range 220V – 240V and 380V – 480V, 50 Hz / 60 Hz.</li><li>High efficiency and motor starting capacity.</li><li>Frame sizes from 2 to 23 available.</li><li>Winding protection for humid environments up to 95 %.</li><li>Compact and rigid assembly for better generator vibrations.</li><li>Steel frame.</li><li>Cast iron flanges and shields.</li><li>Twin and single bearing versions for most engines.</li><li>Half-key balancing.</li><li>Greased for life bearings.</li><li>Easy access to the voltage regulator and connections.</li><li>Choice of accessories for paralleling and measurement.</li><li>Digital AVR adapted to the machine exterior.</li></ul></div>
    <footer class="page__footer"><span class="brandmark" style="left:20px;top:9px"><i></i>NORTHFIELD ENERGY</span></footer>
  </article>
  <article class="page page--right">
    <header class="page__header"><span class="brandmark" style="right:16px;top:13px"><i></i>NORTHFIELD ENERGY</span></header>
    <svg class="deco" viewBox="0 0 280 362">
      <rect x="0" y="27" width="280" height="2" fill="#f7b918"/><rect x="0" y="29" width="280" height="7" fill="#2b2b2d"/>
      <circle cx="135" cy="155" r="62" fill="#f7b918"/>
      <path d="M135 93 H222 V100" fill="none" stroke="#f7b918" stroke-width="1.3"/>
      <rect x="266" y="140" width="3" height="180" fill="#f7b918"/><rect x="272" y="160" width="1.5" height="160" fill="#e8730c"/>
      <rect x="0" y="328" width="280" height="3" fill="#f7b918"/><rect x="0" y="331" width="280" height="7" fill="#2b2b2d"/>
    </svg>
    <h2 class="title">Alternator <b>Parts</b></h2>
    <div class="photo" role="img" aria-label="Photo of an automatic voltage regulator circuit board" style="left:82px;top:100px;width:95px;height:95px;background:linear-gradient(135deg,#3a4250 0%,#1b2230 70%,#e0e0e0 100%)"></div>
    <div class="brandbox" style="left:193px"><span><span class="r">MERIDIAN</span> | <span class="r">KESTREL</span></span><span class="k">LAURENT<br>MOTEURS</span></div>
    <div class="features" style="top:213px"><h4>FEATURES:</h4><ul>
      <li>Class H insulation throughout.</li><li>Standard 12-wire reconnectable winding, 2/3 pitch.</li><li>Voltage range 220V – 240V and 380V – 480V, 50 Hz / 60 Hz.</li><li>High efficiency and motor starting capacity.</li><li>Frame sizes from 2 to 23 available.</li><li>Winding protection for humid environments up to 95 %.</li><li>Compact and rigid assembly for better generator vibrations.</li><li>Steel frame.</li><li>Cast iron flanges and shields.</li><li>Twin and single bearing versions for most engines.</li><li>Half-key balancing.</li><li>Greased for life bearings.</li><li>Easy access to the voltage regulator and connections.</li><li>Choice of accessories for paralleling and measurement.</li><li>Digital AVR adapted to the machine exterior.</li></ul></div>
    <footer class="page__footer"><span class="page__running">DISTRIBUTOR <span>PROGRAM GUIDE</span></span><span class="page__num">9</span></footer>
  </article>
</section>

<!-- Spread 2: pages 10–11 -->
<section class="spread spread--2">
  <article class="page page--left">
    <header class="page__header"><span class="page__num">10</span><span class="page__running">DISTRIBUTOR <span>PROGRAM GUIDE</span></span></header>
    <svg class="deco" viewBox="0 0 280 362">
      <rect x="0" y="27" width="280" height="2" fill="#f7b918"/><rect x="0" y="29" width="280" height="7" fill="#2b2b2d"/>
      <circle cx="140" cy="150" r="62" fill="#f7b918"/>
      <path d="M140 88 H233 V100" fill="none" stroke="#f7b918" stroke-width="1.3"/>
      <rect x="266" y="140" width="3" height="180" fill="#f7b918"/><rect x="272" y="160" width="1.5" height="160" fill="#e8730c"/>
      <rect x="0" y="318" width="280" height="3" fill="#f7b918"/><rect x="0" y="321" width="280" height="6" fill="#2b2b2d"/>
    </svg>
    <h2 class="title"><b>Controllers</b></h2>
    <div class="photo" role="img" aria-label="Photo of a generator control module with display and buttons" style="left:40px;top:92px;width:148px;height:108px;background:linear-gradient(180deg,#2a2a2c 0%,#141416 100%);border-radius:6px"></div>
    <div class="brandbox"><span class="k">DELTA CTRL</span><span class="k">SOLVANE</span></div>
    <div class="features"><h4>FEATURES:</h4><ul>
      <li>Class H insulation throughout.</li><li>Standard 12-wire reconnectable winding, 2/3 pitch.</li><li>Voltage range 220V – 240V and 380V – 480V, 50 Hz / 60 Hz.</li><li>High efficiency and motor starting capacity.</li><li>Frame sizes from 2 to 23 available.</li><li>Winding protection for humid environments up to 95 %.</li><li>Compact and rigid assembly for better generator vibrations.</li><li>Steel frame.</li><li>Cast iron flanges and shields.</li><li>Twin and single bearing versions for most engines.</li><li>Half-key balancing.</li><li>Greased for life bearings.</li><li>Easy access to the voltage regulator and connections.</li><li>Choice of accessories for paralleling and measurement.</li><li>Digital AVR adapted to the machine exterior.</li></ul></div>
    <footer class="page__footer"><span class="brandmark" style="left:20px;top:9px"><i></i>NORTHFIELD ENERGY</span></footer>
  </article>
  <article class="page page--right">
    <header class="page__header"><span class="brandmark" style="right:16px;top:13px"><i></i>NORTHFIELD ENERGY</span></header>
    <svg class="deco" viewBox="0 0 280 362">
      <rect x="0" y="27" width="280" height="2" fill="#f7b918"/><rect x="0" y="29" width="280" height="7" fill="#2b2b2d"/>
      <circle cx="135" cy="155" r="62" fill="#f7b918"/>
      <path d="M135 93 H222 V100" fill="none" stroke="#f7b918" stroke-width="1.3"/>
      <rect x="266" y="140" width="3" height="180" fill="#f7b918"/><rect x="272" y="160" width="1.5" height="160" fill="#e8730c"/>
      <rect x="0" y="328" width="280" height="3" fill="#f7b918"/><rect x="0" y="331" width="280" height="7" fill="#2b2b2d"/>
    </svg>
    <h2 class="title">Transfer <b>Switches</b></h2>
    <div class="photo" role="img" aria-label="Photo of a grey wall-mounted automatic transfer switch cabinet" style="left:60px;top:75px;width:82px;height:170px;background:linear-gradient(90deg,#cfd0cc 0%,#e9e9e6 50%,#c8c8c4 100%)"></div>
    <div class="brandbox" style="left:193px"><span class="r" style="font-size:7px">ARCWAY</span><span class="g">HALDEN</span></div>
    <div class="features" style="top:258px"><h4>FEATURES:</h4><ul>
      <li>Class H insulation throughout.</li><li>Standard 12-wire reconnectable winding, 2/3 pitch.</li><li>Voltage range 220V – 240V and 380V – 480V.</li><li>High efficiency and motor starting capacity.</li><li>Frame sizes from 2 to 23 available.</li><li>Winding protection for humid environments up to 95 %.</li><li>Compact and rigid assembly.</li><li>Steel frame.</li><li>Cast iron flanges and shields.</li><li>Twin and single bearing versions for most engines.</li><li>Half-key balancing.</li><li>Greased for life bearings.</li></ul></div>
    <footer class="page__footer"><span class="page__running">DISTRIBUTOR <span>PROGRAM GUIDE</span></span><span class="page__num">11</span></footer>
  </article>
</section>

<!-- Spread 3: page 12 + closing image -->
<section class="spread spread--3">
  <article class="page page--left">
    <header class="page__header"><span class="page__num">12</span><span class="page__running">DISTRIBUTOR <span>PROGRAM GUIDE</span></span></header>
    <svg class="deco" viewBox="0 0 280 362">
      <rect x="0" y="27" width="280" height="2" fill="#f7b918"/><rect x="0" y="29" width="280" height="7" fill="#2b2b2d"/>
      <rect x="0" y="318" width="280" height="3" fill="#f7b918"/><rect x="0" y="321" width="280" height="6" fill="#2b2b2d"/>
    </svg>
    <h2 class="title" style="top:47px">Our <b>Distributors</b></h2>
    <div class="tag" style="left:33px;top:80px;width:94px">ALTERNATOR &amp; PARTS</div>
    <div class="cols">
      <ul>
        <li>Buy direct from an official master distributor for the Americas.</li>
        <li>Buy direct from an official parts distributor for the Americas.</li>
        <li>Direct access to the largest stock of alternators and parts in the region.</li>
        <li>1 hour response time for quotes during business hours, 8:30 am to 5:30 pm EST.</li>
        <li>Complete online library including data sheets, manuals, diagrams, photos and more.</li>
        <li>Online account access with retail pricing, discounts, order status and order history.</li>
      </ul>
      <ul>
        <li>20-minute response time on all pricing and availability requests, Monday through Saturday.</li>
        <li>Standard same-day shipping on all stock orders (cutoff 4:00 PM EST).</li>
        <li>Extended same-day shipping service available on all stock orders.</li>
        <li>Extended same-day shipping on weekends for urgent orders.</li>
        <li>Worldwide drop-shipping and blind shipping available.</li>
        <li>Lead and customer referral program for qualified accounts.</li>
        <li>Comprehensive online training and certification program.</li>
      </ul>
    </div>
    <div class="tag" style="left:33px;top:196px;width:94px">OUR LOCATION</div>
    <div class="location">
      <p>NORTHFIELD ENERGY is a Florida USA company specialized in the distribution of top quality products for the power generation industry around the world.</p>
      <p>Our main location is conveniently located a short distance from the seaport, the freight district and the international airport.</p>
      <p>Major couriers and hundreds of freight forwarders in the area are close by, guaranteeing easy and competitive access to all major destinations around the world.</p>
    </div>
    <div class="divider"></div>
    <div class="tag" style="left:151px;top:196px;width:100px">CONTACT US TODAY!</div>
    <div class="contact">
      <div class="row"><svg viewBox="0 0 10 10"><path d="M5 0.5a3.3 3.3 0 0 0-3.3 3.3C1.7 6.4 5 9.5 5 9.5s3.3-3.1 3.3-5.7A3.3 3.3 0 0 0 5 .5z" fill="#f7b918"/><circle cx="5" cy="3.8" r="1.2" fill="#fff"/></svg>1200 Harbor Way, Portside, FL 30000</div>
      <div class="row"><svg viewBox="0 0 10 10"><path d="M2 1l2 0 1 2.5-1.2.8a6 6 0 0 0 2 2l.8-1.2L9 6v2c0 .6-.5 1-1 1C4.5 9 1 5.5 1 2c0-.5.4-1 1-1z" fill="#f7b918"/></svg><span>1-800-555-0142 <span style="font-weight:400">(Toll Free)</span></span></div>
      <div class="row"><svg viewBox="0 0 10 10"><circle cx="5" cy="5" r="4" fill="none" stroke="#f7b918" stroke-width="1.2"/><path d="M1 5h8M5 1c-2 2.5-2 5.5 0 8M5 1c2 2.5 2 5.5 0 8" fill="none" stroke="#f7b918" stroke-width=".8"/></svg>www.northfieldenergy-example.com</div>
      <div class="row"><svg viewBox="0 0 10 10"><rect x="1" y="2.5" width="8" height="5.5" fill="#f7b918"/><path d="M1 2.5l4 3 4-3" fill="none" stroke="#fff" stroke-width=".8"/></svg><span>parts@northfieldenergy-example.com<br>alternators@northfieldenergy-example.com<br>transferswitch@northfieldenergy-example.com<br>controls@northfieldenergy-example.com<br>regulators@northfieldenergy-example.com<br>generators@northfieldenergy-example.com<br><br>info@northfieldenergy-example.com</span></div>
    </div>
    <footer class="page__footer"><span class="brandmark" style="left:20px;top:9px"><i></i>NORTHFIELD ENERGY</span></footer>
  </article>
  <article class="page page--right" style="background:#15151d">
    <div class="photo-city" role="img" aria-label="Photo of a city skyline at dusk reflected on the water"></div>
    <svg class="deco" viewBox="0 0 280 362">
      <rect x="0" y="27" width="280" height="2" fill="#f7b918"/>
      <rect x="266" y="140" width="3" height="222" fill="#f7b918"/><rect x="272" y="160" width="1.5" height="202" fill="#e8730c"/>
    </svg>
  </article>
</section>

</body>
</html>
```